Web Page for marketing online agency

We are an online marketing agency that is acing the direct response model. We engage with our customers throughout different marketing techniques as research copy-writing, advertisements and content writing. We would need a website design that will have four main aspects: The Vision; stating who we are, The Mission; stating what we do, The Team And It's Values, and a Contact Form. For this design we would want a sharp, clean and smart approach, with illustrated elements or suggestive images. You can use the attached copy, the logo, the USP and the motto. Please integrate them as you see fit while keeping in mind the previous needs and copy. This website is going to be our connection with our possible partners, future colleagues and even our clients. You may submit a design for one page or integrate the 4 different aspects on separate web pages.
Target Market(s)
business partners, future employees, age range 25-60
Industry/Entity Type
Direct Marketing
Number of Pages Required
1 page
Requirements
Must have
- Menu / Header
- 4 Parts or 4 Pages including: vision, mission, team, contact
- Logo
- Motto: Direct Brilliance
- USP: We help people help themselves.
- The copy attached
Nice to have
- Representative illustrated images or elements
Should not have
- A boring design, classical design - Pagequill like

```html
<!DOCTYPE html>
<html lang="en">
<head>
<meta charset="utf-8">
<title>Brightwell – Direct Brilliance</title>
<link rel="stylesheet" href="https://fonts.googleapis.com/css2?family=Montserrat:wght@400;500;600;700&family=Open+Sans:wght@400;600&display=swap">
<style>
:root{
  --sky:#5ec3f0;
  --blue:#1a9df0;
  --cyan:#00e8e0;
  --ink:#1d1d22;
  --text:#4a4a52;
  --muted:#8a8a92;
  --panel:#f0f0f2;
  --hero:#eeeef1;
  --footer:#2b2b2e;
  --footer-field:#3a3a3e;
  --white:#ffffff;
}
*{box-sizing:border-box;margin:0;padding:0}
html,body{width:1200px;height:2999px;overflow:hidden}
body{position:relative;background:var(--white);font-family:"Open Sans",Arial,sans-serif;color:var(--text)}
.abs{position:absolute}
h1,h2,h3,.brand,.nav a{font-family:"Montserrat",Arial,sans-serif}

/* top bar */
.topbar{left:0;top:0;width:1200px;height:27px;background:var(--sky);color:var(--white);font-size:9px}
.topbar .contact{position:absolute;left:752px;top:8px;display:flex;gap:22px;align-items:center}
.topbar .contact span{display:flex;gap:6px;align-items:center}
.topbar .social{position:absolute;left:978px;top:9px;display:flex;gap:7px}
.topbar .social i{display:block;width:9px;height:9px;border-radius:50%;background:var(--white)}

/* header */
.header{left:0;top:27px;width:1200px;height:55px;background:var(--white)}
.brand{position:absolute;left:164px;top:14px;display:flex;align-items:center;gap:6px;font-size:21px;font-weight:600;color:var(--ink)}
.brand .dot{width:14px;height:14px;border-radius:50%;background:var(--blue)}
.nav{position:absolute;left:775px;top:22px;display:flex;gap:32px}
.nav a{font-size:11px;font-weight:600;color:var(--ink);text-decoration:none}

/* hero */
.hero{left:0;top:82px;width:1200px;height:431px;background:var(--hero);overflow:hidden}
.hero-photo{position:absolute;left:492px;top:0;width:708px;height:431px;background:linear-gradient(100deg,#f1f1f3 0%,#d9dde3 35%,#b8c1cc 70%,#eef0f3 100%)}
.hero h1{position:absolute;left:164px;top:138px;font-size:31px;line-height:38px;font-weight:700;letter-spacing:2px;color:var(--ink)}
.hero .usp{position:absolute;left:164px;top:222px;font-size:12px;letter-spacing:1px;color:var(--muted)}
.btn{position:absolute;left:164px;top:279px;width:121px;height:27px;background:linear-gradient(90deg,var(--blue),var(--cyan));color:var(--white);font:600 10px "Montserrat",Arial,sans-serif;display:flex;align-items:center;justify-content:center}
.hero-wave{position:absolute;left:0;bottom:0}

/* cards */
.card{top:593px;width:224px;height:184px;background:var(--panel);text-align:center;padding:24px 20px 0}
.card svg{display:block;margin:0 auto 10px}
.card h3{font-size:14px;font-weight:600;color:var(--ink);margin-bottom:12px}
.card p{font-size:8px;line-height:13px;color:var(--text)}
.card.active{background:linear-gradient(135deg,var(--blue),var(--cyan))}
.card.active h3,.card.active p{color:var(--white)}
.card.active p{font-weight:600}

/* vision */
.vision-title{left:162px;top:938px;font-size:22px;font-weight:500;color:var(--ink)}
.vision-lead{left:162px;top:986px;width:310px;font-size:14px;line-height:21px;color:var(--ink)}
.vision-body{left:162px;top:1095px;width:360px;font-size:9px;line-height:15px;color:var(--muted)}
.read-more{left:162px;top:1240px;font-size:10px;color:var(--blue)}
.vision-art{left:600px;top:913px;width:400px;height:320px;border-radius:24px;background:linear-gradient(135deg,#eaf6fd 0%,#cdeaf9 50%,#e6f5fc 100%)}

.divider{left:0;top:1332px}

/* mission */
.mission-title{left:254px;top:1456px;font-size:21px;font-weight:500;color:var(--ink)}
.rule{height:4px;width:103px;background:linear-gradient(90deg,var(--blue),var(--cyan))}
.feature-title{font-size:20px;font-weight:500;color:var(--ink)}
.feature-text{font-size:14px;line-height:22px;color:var(--ink);width:240px}
.photo{border-radius:3px}
.photo-desk{left:609px;top:1520px;width:355px;height:248px;background:linear-gradient(135deg,#d9c3a8,#a88462 55%,#6c5646)}
.photo-meeting{left:234px;top:1770px;width:355px;height:248px;background:linear-gradient(135deg,#8e8f92,#d8d8da 45%,#b9433f 80%,#5a5b60)}

/* team */
.team{left:0;top:2082px;width:1200px;height:441px;background:linear-gradient(100deg,#169cf0 0%,#0bc4ee 50%,#02ece0 100%);overflow:hidden;color:var(--white)}
.team h2{position:absolute;left:0;width:1200px;top:68px;text-align:center;font-size:20px;font-weight:500}
.team .underline{position:absolute;left:582px;top:112px;width:36px;height:3px;background:var(--white)}
.member{position:absolute;top:190px;display:flex;gap:18px}
.avatar{width:74px;height:74px;border-radius:50%;border:4px solid var(--white);background:linear-gradient(135deg,#c9ced6,#7d848f);flex:none}
.member h3{font-size:10px;font-weight:700;margin-top:10px}
.member .role{font-size:8px;font-weight:600;margin:4px 0 14px}
.member p{font-size:9px;line-height:14px;font-weight:600;width:268px}

/* map */
.map{left:0;top:2523px;width:1200px;height:312px;background:linear-gradient(160deg,#efefef,#e2e2e2 50%,#ececec)}
.address{left:486px;top:2699px;width:140px;height:46px;background:var(--white);font-size:8px;line-height:12px;color:var(--muted);padding:9px 12px;box-shadow:0 2px 6px rgba(0,0,0,.12)}
.map-btn{top:2751px;width:40px;height:40px;border-radius:4px;display:flex;align-items:center;justify-content:center;background:var(--white);box-shadow:0 2px 6px rgba(0,0,0,.15)}
.map-btn.on{background:var(--blue)}

/* footer */
.footer{left:0;top:2835px;width:1200px;height:164px;background:var(--footer)}
.footer .social{position:absolute;left:250px;top:60px;display:flex;gap:30px}
.footer .social i{display:block;width:14px;height:14px;border-radius:3px;background:#45454a}
.newsletter{position:absolute;left:595px;top:53px;width:369px;height:39px;background:var(--footer-field);border-radius:3px;display:flex;align-items:center;padding:0 12px;font-size:9px;color:#a8a8ae;gap:14px}
.newsletter .join{margin-left:auto;background:#4d4d52;color:var(--white);font-size:9px;padding:6px 12px;border-radius:2px}
.copyright{position:absolute;left:240px;top:134px;font-size:8px;color:#6a6a70}
.footer-nav{position:absolute;left:742px;top:133px;display:flex;gap:24px}
.footer-nav a{font-size:9px;color:#d8d8dc;text-decoration:none;font-family:"Montserrat",Arial,sans-serif}
</style>
</head>
<body>

<div class="abs topbar">
  <div class="contact">
    <span><svg width="9" height="9" viewBox="0 0 24 24"><path fill="#fff" d="M6.6 10.8a15 15 0 0 0 6.6 6.6l2.2-2.2a1 1 0 0 1 1-.3 11 11 0 0 0 3.6.6 1 1 0 0 1 1 1V20a1 1 0 0 1-1 1A17 17 0 0 1 3 4a1 1 0 0 1 1-1h3.5a1 1 0 0 1 1 1c0 1.2.2 2.4.6 3.6a1 1 0 0 1-.3 1z"/></svg>+00 555 0142</span>
    <span><svg width="10" height="8" viewBox="0 0 24 18"><rect x="1" y="1" width="22" height="16" rx="2" fill="none" stroke="#fff" stroke-width="2"/><path d="M1 2l11 8 11-8" fill="none" stroke="#fff" stroke-width="2"/></svg>hello@brightwellmail.com</span>
  </div>
  <div class="social"><i></i><i></i><i></i><i></i></div>
</div>

<header class="abs header">
  <div class="brand">Brightwell<span class="dot"></span></div>
  <nav class="nav"><a href="#">Home</a><a href="#">Vision</a><a href="#">Mission</a><a href="#">Team</a><a href="#">Contact</a></nav>
</header>

<section class="abs hero">
  <div class="hero-photo" role="img" aria-label="Photo of business people reviewing printed charts next to a laptop"></div>
  <h1>BRIGHTWELL -<br>DIRECT BRILLIANCE</h1>
  <p class="usp">We help people help themselves.</p>
  <span class="btn">Read more</span>
  <svg class="hero-wave" width="1200" height="110" viewBox="0 0 1200 110" preserveAspectRatio="none">
    <defs><linearGradient id="waveA" x1="0" x2="1"><stop offset="0" stop-color="#1a9df0" stop-opacity=".35"/><stop offset="1" stop-color="#00e8e0" stop-opacity=".6"/></linearGradient>
    <linearGradient id="waveB" x1="0" x2="1"><stop offset="0" stop-color="#5ec3f0"/><stop offset="1" stop-color="#00e8e0"/></linearGradient></defs>
    <path d="M0 60 C120 20 240 20 360 55 S600 100 760 60 1000 10 1200 50 V110 H0Z" fill="url(#waveA)"/>
    <path d="M0 85 C150 55 300 60 450 80 S750 100 900 78 1100 60 1200 72 V110 H0Z" fill="url(#waveB)"/>
  </svg>
</section>

<div class="abs card active" style="left:164px">
  <svg width="40" height="30" viewBox="0 0 40 30"><path d="M3 17 Q20 2 37 17 Q20 30 3 17Z" fill="none" stroke="#fff" stroke-width="2"/><circle cx="20" cy="17" r="5" fill="none" stroke="#fff" stroke-width="2"/><path d="M20 1v4M10 4l2 3M30 4l-2 3" stroke="#fff" stroke-width="2"/></svg>
  <h3>Vision</h3>
  <p>We are a direct response company that creates and sells information products and services that millions of people find interesting and important in their lives.</p>
</div>
<div class="abs card" style="left:486px">
  <svg width="40" height="30" viewBox="0 0 40 30"><circle cx="20" cy="15" r="13" fill="none" stroke="#1d1d22" stroke-width="2"/><path d="M9 23 L18 12 L23 18 L26 15 L31 23" fill="none" stroke="#1d1d22" stroke-width="2"/><path d="M20 4v6" stroke="#1d1d22" stroke-width="2"/></svg>
  <h3>Mission</h3>
  <p>We get our inspiration from modern heroes and make their stories available for others.</p>
</div>
<div class="abs card" style="left:810px">
  <svg width="44" height="30" viewBox="0 0 44 30"><g fill="none" stroke="#1d1d22" stroke-width="2"><circle cx="12" cy="9" r="4"/><circle cx="22" cy="8" r="4"/><circle cx="32" cy="9" r="4"/><path d="M4 26v-5a5 5 0 0 1 10 0v5M14 26v-6a6 6 0 0 1 12 0v6M26 26v-5a5 5 0 0 1 10 0v5"/></g></svg>
  <h3>Team</h3>
  <p>We're a small team of smart, funny hard-working specialists who are pushing to become the #1 company in self-reliance.</p>
</div>

<h2 class="abs vision-title">Who we are? Our vision:</h2>
<p class="abs vision-lead">We are a direct response company that creates and sells information products and services that millions of people find interesting and important in their lives.</p>
<p class="abs vision-body">We are specialized in the self-reliance market and we serve conservative Americans.We are in this business to serve globally and to grow individually.<br>What we serve and inspire are people who need safety, comfort and peace of mind.We deliver empowerment through products that create fertile shortcuts to solutions, disentangle reality, simplify choices and ultimately make lives better.<br>We give reassurance and confidence to these people through fresh, unique solutions.We get our inspiration from modern heroes and make their stories available for others.</p>
<a class="abs read-more">Read more</a>
<div class="abs vision-art" role="img" aria-label="Illustration of a laptop showing the website homepage, set among soft blue decorative shapes"></div>

<svg class="abs divider" width="1200" height="40" viewBox="0 0 1200 40" preserveAspectRatio="none"><path d="M0 22 C200 8 400 30 600 18 S1000 8 1200 22" fill="none" stroke="#e3e6ea" stroke-width="2"/></svg>

<h2 class="abs mission-title">What is it that we do? Our mission</h2>
<div class="abs rule" style="left:267px;top:1557px"></div>
<h3 class="abs feature-title" style="left:267px;top:1588px">Great Information</h3>
<p class="abs feature-text" style="left:267px;top:1627px">We create and aggregate great information products</p>
<div class="abs photo photo-desk" role="img" aria-label="Photo of a person working on a laptop at a wooden desk"></div>
<div class="abs photo photo-meeting" role="img" aria-label="Photo of two colleagues working on laptops at a white table"></div>
<div class="abs rule" style="left:642px;top:1807px"></div>
<h3 class="abs feature-title" style="left:642px;top:1838px">Compels People to act</h3>
<p class="abs feature-text" style="left:642px;top:1876px">We write content that compels people to act</p>

<section class="abs team">
  <svg class="abs" style="left:0;bottom:0" width="1200" height="120" viewBox="0 0 1200 120" preserveAspectRatio="none"><path d="M0 70 C200 30 400 40 600 70 S1000 100 1200 60 V120 H0Z" fill="#ffffff" fill-opacity=".08"/><path d="M0 95 C250 70 450 80 700 95 S1050 100 1200 85 V120 H0Z" fill="#ffffff" fill-opacity=".08"/></svg>
  <h2>Our Team &amp; Values</h2>
  <div class="underline"></div>
  <div class="member" style="left:248px">
    <div class="avatar" role="img" aria-label="Portrait of Dorin Vale"></div>
    <div>
      <h3>DORIN VALE</h3>
      <div class="role">CEO Brightwell</div>
      <p>Dorin started or was involved in 15 failed businesses before discovering online copywriting. After that, he ended up writing for Keller Inc. and did 10-12 "successful" projects there, at least 3 of which broke the million dollar mark. He wrote the famous HearthPower, and the infamous QuietEar Plan and Harlan Motor sales letters.</p>
    </div>
  </div>
  <div class="member" style="left:624px">
    <div class="avatar" role="img" aria-label="Portrait of Mihai Vale"></div>
    <div>
      <h3>MIHAI VALE</h3>
      <div class="role">Cofounder &amp; Affiliate Manager Brightwell</div>
      <p>Since the company's late 2012 start, Mihai grew a network of 5000 affiliates, that dominates OfferHub's survival niche - 3 out of top 5 products are Brightwell offers, under the Stayready brand.</p>
    </div>
  </div>
</section>

<div class="abs map" role="img" aria-label="Street map showing the office location"></div>
<svg class="abs" style="left:670px;top:2589px" width="54" height="70" viewBox="0 0 54 70"><path d="M27 68 C10 46 3 36 3 25 A24 24 0 0 1 51 25 C51 36 44 46 27 68Z" fill="#1a9df0"/><circle cx="27" cy="25" r="12" fill="#fff"/></svg>
<div class="abs address">418 Linden Row<br>Eastmoor, Northvale</div>
<div class="abs map-btn on" style="left:537px"><svg width="16" height="20" viewBox="0 0 16 20"><path d="M8 19C3 13 1 10 1 7a7 7 0 0 1 14 0c0 3-2 6-7 12Z" fill="none" stroke="#fff" stroke-width="1.6"/><circle cx="8" cy="7" r="2.5" fill="none" stroke="#fff" stroke-width="1.6"/></svg></div>
<div class="abs map-btn" style="left:584px"><svg width="20" height="15" viewBox="0 0 20 15"><rect x="1" y="1" width="18" height="13" rx="1" fill="none" stroke="#333" stroke-width="1.4"/><path d="M1 2l9 7 9-7" fill="none" stroke="#333" stroke-width="1.4"/></svg></div>
<div class="abs map-btn" style="left:631px"><svg width="18" height="18" viewBox="0 0 24 24"><path d="M6.6 10.8a15 15 0 0 0 6.6 6.6l2.2-2.2a1 1 0 0 1 1-.3 11 11 0 0 0 3.6.6 1 1 0 0 1 1 1V20a1 1 0 0 1-1 1A17 17 0 0 1 3 4a1 1 0 0 1 1-1h3.5a1 1 0 0 1 1 1c0 1.2.2 2.4.6 3.6a1 1 0 0 1-.3 1z" fill="none" stroke="#333" stroke-width="1.6"/></svg></div>

<footer class="abs footer">
  <div class="social"><i></i><i></i><i></i><i></i></div>
  <div class="newsletter">
    <svg width="18" height="13" viewBox="0 0 18 13"><rect x="1" y="1" width="16" height="11" rx="1" fill="none" stroke="#a8a8ae" stroke-width="1.3"/><path d="M1 2l8 5 8-5" fill="none" stroke="#a8a8ae" stroke-width="1.3"/></svg>
    <span>Enter your email for our newsletter</span>
    <span class="join">Join</span>
  </div>
  <div class="copyright">© Copyright 2018</div>
  <nav class="footer-nav"><a href="#">Home</a><a href="#">Vision</a><a href="#">Mission</a><a href="#">Team</a><a href="#">Contact</a></nav>
</footer>

</body>
</html>
```